Echoes Over Quiet Harbours - Leo Fenwright - CD Cover Design Project

Single Cover for CD & Online media e.g. Tunevault Graphics

The first Album release from Leo Fenwright will be Titled 'Echoes Over Quiet Harbours'.

For the release the Album requires artwork that is eye catching, seriously professional & meets the requirements of Disc Pony, Tunevault and also a physical copy on CD.

see details in this link:
http://members.discpony.example/faq.aspx
http://selfmadesound.discpony.example/2009/11/avoid-album-art-atrocities/
http://replies.quorvex.example/question/index?qid=20111015141433AAdDTmH

Please find all files you need to get started and a mini mix of the album tracks in this file crate
https://www.filecrate.example/sh/k8w4tnzqplumvd7/9yHkRmT5aQ

Any advice on this would be greatly appreciated,

I would also like the two logo's I have uploaded to be used,
one is the Leo Fenwright logo and the other is for Hollins & Webb Records logo (please remove the R and replace with a C for copyright.)

I would like the Leo Fenwright logo to feature a heart instead of the tie.

I have uploaded pictures of Leo Fenwright and another zip file of many others, it would be nice to include one of these maybe on the 2nd page or back of the CD. Please don't use them as the front cover.

I would like the cover layout to be similar layout to the previous Single cover for 'Every River Finds the Sea'. Bar of colour down the side featuring the Leo Fenwright logo and title below with picture to the side. I am open to new ideas for the layout but want to create some unity to make the artists and his work easily recognizable

If you submit a design please don't delete the raw file ideas as I may ask you to revert to one of these ideas.

Good Luck
Updates

I would proffer an illustrated design 

Please leave the Hollins & Webb Logo off the front cover, (should be on the back of the CD cover)

I have uploaded the previous CD's cover layout to help show what I am looking for, some of the covers are looking very good, please remember illustrated covers proffered.

```html
<!DOCTYPE html>
<html lang="en">
<head>
<meta charset="utf-8">
<title>Echoes Over Quiet Harbours – Leo Fenwright – CD Cover</title>
<link rel="stylesheet" href="https://fonts.googleapis.com/css2?family=Lato:wght@400;700;900&family=Russo+One&family=Kaushan+Script&display=swap">
<style>
  :root {
    --canvas: #f2f0f1;
    --ink: #111014;
    --pink-light: #f2609a;
    --pink: #e0407a;
    --pink-deep: #8c1d48;
    --white: #ffffff;
    --night: #0c0b0d;
    --smoke: #3a3639;
    --skin-shadow: #4a2c2a;
    --jacket: #1b1d24;
  }
  * { box-sizing: border-box; margin: 0; padding: 0; }
  html, body {
    width: 1200px; height: 750px; overflow: hidden;
    background: var(--canvas);
    font-family: "Lato", sans-serif;
  }
  .spread {
    position: relative; width: 1200px; height: 750px;
    display: flex; justify-content: center; align-items: center; gap: 40px;
  }
  .cover {
    position: relative; width: 540px; height: 540px; overflow: hidden;
    background: var(--night);
    box-shadow: 0 6px 18px rgba(0,0,0,0.25);
  }

  /* Front */
  .front-artwork {
    position: absolute; left: 0; top: 0; width: 62%; height: 100%;
    background:
      radial-gradient(ellipse at 55% 40%, var(--skin-shadow) 0%, transparent 55%),
      radial-gradient(ellipse at 50% 90%, var(--jacket) 0%, transparent 60%),
      linear-gradient(160deg, #2a2426 0%, var(--night) 70%);
  }
  .title-bar {
    position: absolute; right: 0; top: 0; width: 38%; height: 100%;
    background: linear-gradient(180deg, var(--pink-light) 0%, var(--pink) 45%, var(--pink-deep) 100%);
    display: flex; flex-direction: column; align-items: center;
    padding: 40px 12px 0;
  }
  .artist-mark {
    display: flex; flex-direction: column; align-items: center; gap: 10px;
    margin-bottom: 48px;
  }
  .artist-mark__square {
    width: 58px; height: 58px; background: var(--ink);
  }
  .artist-mark__name {
    font-family: "Lato", sans-serif; font-weight: 900;
    color: var(--ink); font-size: 26px; line-height: 0.95;
    text-align: center; text-transform: uppercase;
  }
  .album-title {
    font-family: "Russo One", sans-serif; font-weight: 400;
    color: var(--white); text-transform: uppercase; line-height: 1.05;
    align-self: stretch; text-align: left; padding-left: 4px;
  }
  .album-title span {
    display: block; white-space: nowrap;
    text-shadow: 2px 2px 0 var(--ink);
  }
  .album-title .big { font-size: 36px; }
  .album-title .mid { font-size: 22px; margin: 6px 0; }
  .album-title .small { font-size: 28px; }

  /* Back */
  .back-backdrop {
    position: absolute; inset: 0;
    background:
      radial-gradient(ellipse at 70% 25%, #5a5357 0%, transparent 55%),
      radial-gradient(ellipse at 20% 80%, #2c2729 0%, transparent 60%),
      linear-gradient(180deg, var(--smoke) 0%, var(--night) 80%);
  }
  .label-mark {
    position: absolute; top: 22px; right: 22px;
    display: flex; flex-direction: column; align-items: center; gap: 6px;
  }
  .label-mark__square { width: 34px; height: 34px; background: var(--pink); }
  .label-mark__name {
    font-family: "Lato", sans-serif; font-weight: 700; font-size: 10px;
    color: var(--white); text-transform: uppercase; text-align: center; line-height: 1.2;
  }
  .liner-note {
    position: absolute; left: 0; top: 170px; width: 350px;
    padding: 14px 18px;
    background: linear-gradient(90deg, rgba(224,64,122,0.35), rgba(224,64,122,0.05));
    color: var(--white); font-size: 14.5px; line-height: 1.4; text-align: justify;
  }
  .artist-photo {
    position: absolute; right: 40px; top: 160px; width: 110px; height: 330px;
    background: linear-gradient(180deg, #5a4a42 0%, var(--jacket) 30%, #1c2438 75%, #15151a 100%);
    border-radius: 40px 40px 10px 10px;
    opacity: 0.9;
  }
  .back-band {
    position: absolute; left: 0; bottom: 0; width: 100%; height: 64px;
    background: linear-gradient(180deg, var(--pink-light) 0%, var(--pink) 50%, var(--pink-deep) 100%);
    display: flex; align-items: center; padding-left: 14px;
  }
  .back-band__title {
    font-family: "Kaushan Script", cursive; color: var(--white);
    font-size: 30px; text-shadow: 2px 2px 0 var(--ink); white-space: nowrap;
  }
</style>
</head>
<body>
  <main class="spread">
    <section class="cover cover--front" aria-label="Front cover">
      <div class="front-artwork" role="img" aria-label="Illustrated portrait of the artist in sunglasses holding a vintage telephone receiver"></div>
      <div class="title-bar">
        <div class="artist-mark">
          <div class="artist-mark__square"></div>
          <p class="artist-mark__name">Leo<br>Fenwright</p>
        </div>
        <h1 class="album-title">
          <span class="big">Echoes</span>
          <span class="mid">Over Quiet</span>
          <span class="small">Harbours</span>
        </h1>
      </div>
    </section>

    <section class="cover cover--back" aria-label="Back cover">
      <div class="back-backdrop" role="img" aria-label="Smoky dark background with drifting music notes"></div>
      <div class="label-mark">
        <div class="label-mark__square"></div>
        <p class="label-mark__name">Hollins &amp; Webb<br>Records</p>
      </div>
      <p class="liner-note">Lorem Ipsum is simply dummy text of the printing and typesetting industry. Lorem Ipsum has been the industry's standard dummy text ever since the 1500s, when an unknown printer took a galley of type and scrambled it to make a type specimen book. It has survived not only five centuries.</p>
      <div class="artist-photo" role="img" aria-label="Full-length photo of the artist in a leather jacket holding a telephone"></div>
      <div class="back-band">
        <p class="back-band__title">Echoes Over Quiet Harbours</p>
      </div>
    </section>
  </main>
</body>
</html>
```